Ad Banner for knowledge management portal - Benefit of Knowledge Management

This banner is used in a knowledge management web portal.
1. Banner size: 940x380
2. Business background: Provides maintenance, design and engineering, construction, machinery operation, material procurement and production management services for petrochemical and refinery business
3. We would like to see designs that promote the benefit of knowledge managment. "Knowledge of each individuals can be connected to build a greater benefit to the organization"
4. Key message in the banner:
- Knowledge
- Connected
- Team

Industry/Entity Type

Business

Requirements
Should not have
• Do not include picture of real people in the banner

```html
<!DOCTYPE html>
<html lang="en">
<head>
<meta charset="utf-8">
<title>Benefit of Knowledge Management – Banner</title>
<link rel="stylesheet" href="https://fonts.googleapis.com/css2?family=Roboto+Condensed:wght@300;400&display=swap">
<style>
  :root {
    --page-bg: #eeeeee;
    --banner-dark: #05070f;
    --banner-navy: #0a1230;
    --electric-blue: #1f3fd6;
    --sky-blue: #3a8ee8;
    --glow-cyan: #6fc3ff;
    --text-white: #ffffff;
  }
  html, body {
    margin: 0;
    padding: 0;
    width: 1200px;
    height: 1000px;
    overflow: hidden;
    background: var(--page-bg);
  }
  .banner {
    position: absolute;
    left: 248px;
    top: 358px;
    width: 705px;
    height: 285px;
    overflow: hidden;
    background: linear-gradient(100deg, var(--banner-dark) 0%, var(--banner-dark) 45%, var(--banner-navy) 75%, #123a8a 100%);
    font-family: "Roboto Condensed", sans-serif;
    color: var(--text-white);
  }
  .tech-visual {
    position: absolute;
    right: 0;
    top: 0;
    width: 340px;
    height: 210px;
    background:
      radial-gradient(ellipse at 70% 35%, rgba(111,195,255,0.75) 0%, rgba(58,142,232,0.45) 35%, rgba(31,63,214,0.15) 65%, rgba(5,7,15,0) 85%);
  }
  .swooshes {
    position: absolute;
    left: 0;
    top: 0;
    width: 705px;
    height: 285px;
  }
  .headline {
    position: absolute;
    left: 33px;
    top: 26px;
    margin: 0;
    font-weight: 300;
    font-size: 24.5px;
    line-height: 27px;
    letter-spacing: -0.2px;
  }
  .benefits {
    position: absolute;
    left: 36px;
    top: 105px;
    margin: 0;
    padding: 0;
    list-style: none;
    font-weight: 300;
    font-size: 15.5px;
    line-height: 23.8px;
    letter-spacing: -0.2px;
  }
  .benefits li {
    position: relative;
    padding-left: 14px;
  }
  .benefits li::before {
    content: "";
    position: absolute;
    left: 0;
    top: 9px;
    width: 7px;
    height: 7px;
    border-radius: 50%;
    background: var(--text-white);
  }
</style>
</head>
<body>
  <section class="banner">
    <div class="tech-visual" role="img" aria-label="Glowing blue digital panels with data readouts and an upward arrow, suggesting connected knowledge"></div>

    <svg class="swooshes" viewBox="0 0 705 285" aria-hidden="true">
      <defs>
        <linearGradient id="blueBand" x1="0" y1="0" x2="1" y2="0">
          <stop offset="0" stop-color="#1f3fd6" stop-opacity="0.9"/>
          <stop offset="0.6" stop-color="#1a3db8"/>
          <stop offset="1" stop-color="#3a8ee8"/>
        </linearGradient>
        <linearGradient id="whiteBand" x1="0" y1="0" x2="1" y2="0">
          <stop offset="0" stop-color="#ffffff"/>
          <stop offset="0.5" stop-color="#e6e9f2"/>
          <stop offset="1" stop-color="#ffffff"/>
        </linearGradient>
        <radialGradient id="leftGlow" cx="0.2" cy="0.5" r="0.6">
          <stop offset="0" stop-color="#2746e0" stop-opacity="0.8"/>
          <stop offset="1" stop-color="#2746e0" stop-opacity="0"/>
        </radialGradient>
      </defs>
      <ellipse cx="120" cy="235" rx="260" ry="45" fill="url(#leftGlow)"/>
      <path d="M0 240 C 220 265, 480 220, 705 140 L705 160 C 480 240, 220 275, 0 258 Z" fill="url(#whiteBand)"/>
      <path d="M0 258 C 220 275, 480 240, 705 160 L705 200 C 480 255, 260 285, 120 285 L0 285 Z" fill="#05070f"/>
      <path d="M380 285 C 500 270, 620 235, 705 200 L705 285 Z" fill="url(#blueBand)"/>
      <path d="M0 262 C 60 272, 120 280, 170 285 L0 285 Z" fill="#ffffff"/>
    </svg>

    <h1 class="headline">Knowledge of each individual can be connected<br>to build a greater benefit to the organization</h1>

    <ul class="benefits">
      <li>Improved and accelerated Learning</li>
      <li>Enhanced team collaboration &amp; coordination</li>
      <li>Improved the flow of knowledge</li>
      <li>Better knowledge transfer in executing projects</li>
      <li>Extend the global reach, richness, and scope of the organization</li>
    </ul>
  </section>
</body>
</html>
```